Brume vodka

With the logo attached in the subsequent file, a business card that reflects a premium and organic vodka. On the first side, the company logo in large. The names must be included on the back of the card (Miguel Ángel Tomás Ferrandis with the number +34 655 271 389 and Pau Berenguer Casals and +34 677 314 920). The slogan "What binds us" and "Organic and permium vodka" in bold E-mail (brumevodka@mailfield.net); Website www.brumevodkaorg.net

```html
<!DOCTYPE html>
<html lang="en">
<head>
<meta charset="utf-8">
<title>Brume vodka – business card</title>
<link rel="stylesheet" href="https://fonts.googleapis.com/css2?family=Cinzel:wght@400&family=Montserrat:wght@400&display=swap">
<style>
  :root {
    --backdrop: #6e4a33;
    --card: #ffffff;
    --ink-name: #6c6c6c;
    --ink-detail: #878787;
    --ink-brand: #8e8e90;
    --card-shadow: rgba(0, 0, 0, 0.45);
  }
  * { margin: 0; padding: 0; box-sizing: border-box; }
  html, body {
    width: 1200px;
    height: 1000px;
    overflow: hidden;
    background: var(--backdrop);
  }
  .canvas {
    position: relative;
    width: 1200px;
    height: 1000px;
  }
  .card {
    position: absolute;
    left: 266px;
    width: 666px;
    height: 397px;
    background: var(--card);
    box-shadow: 0 3px 8px var(--card-shadow);
  }
  .card--contacts { top: 74px; }
  .card--brand { top: 533px; }

  .contacts {
    position: absolute;
    left: 46px;
    top: 130px;
    font-family: "Montserrat", sans-serif;
    color: var(--ink-detail);
  }
  .person + .person { margin-top: 16px; }
  .person__name {
    font-family: "Cinzel", serif;
    font-size: 22px;
    line-height: 28px;
    color: var(--ink-name);
    letter-spacing: 0.3px;
  }
  .person__phone {
    font-size: 16px;
    line-height: 24px;
    margin-top: 2px;
    letter-spacing: 0.4px;
  }
  .company-links {
    margin-top: 18px;
    font-size: 16px;
    line-height: 26px;
    letter-spacing: 0.2px;
  }

  .brand {
    position: absolute;
    left: 0;
    right: 0;
    top: 150px;
    text-align: center;
    font-family: "Cinzel", serif;
    color: var(--ink-brand);
  }
  .brand__name {
    font-size: 104px;
    line-height: 104px;
    letter-spacing: 2px;
  }
  .brand__sub {
    font-size: 26px;
    line-height: 30px;
    letter-spacing: 6px;
    margin-top: 4px;
  }
  .tagline {
    position: absolute;
    left: 0;
    right: 0;
    top: 347px;
    text-align: center;
    font-family: "Montserrat", sans-serif;
    font-size: 16px;
    color: var(--ink-detail);
    letter-spacing: 0.3px;
  }
</style>
</head>
<body>
<div class="canvas">
  <section class="card card--contacts">
    <div class="contacts">
      <div class="person">
        <p class="person__name">Miguel Ángel<br>Tomás Ferrandis</p>
        <p class="person__phone">+34 655 271 389</p>
      </div>
      <div class="person">
        <p class="person__name">Pau Berenguer Casals</p>
        <p class="person__phone">+34 677 314 920</p>
      </div>
      <div class="company-links">
        <p>brumevodka@mailfield.net</p>
        <p>www.brumevodkaorg.net</p>
      </div>
    </div>
  </section>

  <section class="card card--brand">
    <div class="brand">
      <p class="brand__name">BRUME</p>
      <p class="brand__sub">VODKA</p>
    </div>
    <p class="tagline">Organic and Permium vodka</p>
  </section>
</div>
</body>
</html>
```